Need simple and modern looking business card with all my information on one side and logo on the other side
Info :
Company name - VELMAR CONSTRUCTION LLC
Company addres- 418 harbor 87th. Dunmoor park ny 10352
Email- velmarllc@tridomail.Com
Company phone number 555-318-6094
Cell number- 555-742-0583
Web site - velmarllc.Com
My name Gerald tomasino

Target Market(s)

Construction , home improvement, remodeling

Industry/Entity Type

Construction

Contact Information for Business Card

It has to be moder but at the same time simple

Font styles to use
Sans Serif

Colors
0255a3
ffffff
000000
f78f20
b1b1b1
9d9d9d
1b1b1b
33a6d7
ec1f27

Requirements
Must have
• My logo on one side maybe with a some kind of background on the other side all my information
Nice to have
• Some kind of background pictures provided by you .PLEASE HAVE ACCOUNT WITH PIXELVAULT WILL NOT PAY ANY EXTRA FEES .
Should not have
• Any kind of hamer, nails,screws, helmets itp. Please do not copy the other designs come up with something new.

```html
<!DOCTYPE html>
<html lang="en">
<head>
<meta charset="utf-8">
<title>Velmar Construction LLC — Business Card</title>
<link rel="stylesheet" href="https://fonts.googleapis.com/css2?family=Montserrat:wght@800&family=Quicksand:wght@500;600&display=swap">
<style>
  :root {
    --orange: #f78f20;
    --black: #1b1b1b;
    --ink: #000000;
    --white: #ffffff;
    --grey-light: #b1b1b1;
    --grey-mid: #9d9d9d;
    --sky: #33a6d7;
    --blue: #0255a3;
    --red: #ec1f27;
    --stage: #ecebe8;
  }
  * { box-sizing: border-box; margin: 0; padding: 0; }
  html, body { width: 1200px; height: 780px; overflow: hidden; }
  body {
    background: var(--stage);
    font-family: "Quicksand", sans-serif;
    position: relative;
  }
  .card {
    position: absolute;
    top: 240px;
    width: 525px;
    height: 300px;
    border-radius: 3px;
    overflow: hidden;
    box-shadow: 0 10px 28px rgba(0,0,0,.18);
  }

  /* Front: contact side */
  .card--front { left: 45px; background: var(--white); display: flex; }
  .front-photo {
    width: 205px;
    height: 100%;
    background: linear-gradient(180deg, #4f8fd0 0%, #8fb6dc 38%, #b8a98f 70%, #cdbb98 100%);
    border-right: 4px solid var(--orange);
  }
  .front-info { flex: 1; padding: 30px 26px 0 30px; }
  .company-name {
    font-family: "Montserrat", sans-serif;
    font-weight: 800;
    color: var(--black);
    line-height: 1;
  }
  .company-name__main { display: block; font-size: 40px; letter-spacing: 1px; }
  .company-name__sub { display: block; font-size: 11.5px; letter-spacing: .6px; margin-top: 4px; }
  .person-name {
    color: var(--orange);
    font-size: 19px;
    font-weight: 500;
    margin: 18px 0 12px;
  }
  .address { color: var(--black); font-size: 14px; line-height: 1.3; margin-bottom: 8px; }
  .contact-row { display: flex; align-items: flex-start; gap: 10px; }
  .icon-col { display: flex; flex-direction: column; gap: 4px; padding-top: 2px; }
  .icon-col svg { width: 16px; height: 16px; display: block; }
  .contact-list { list-style: none; color: var(--black); font-size: 14px; line-height: 1.3; }

  /* Back: brand side */
  .card--back {
    left: 630px;
    background: radial-gradient(circle at 55% 45%, #f7f7f7 0%, #e4e4e4 60%, #d2d2d2 100%);
    display: flex;
    align-items: center;
    justify-content: center;
  }
  .brand { display: flex; align-items: center; gap: 14px; }
  .brand__square { width: 22px; height: 22px; background: var(--orange); }
  .brand__name {
    font-family: "Montserrat", sans-serif;
    font-weight: 800;
    color: var(--black);
    line-height: 1;
  }
  .brand__name span { display: block; }
  .brand__main { font-size: 50px; letter-spacing: 3px; }
  .brand__sub { font-size: 14px; letter-spacing: 2.4px; margin-top: 6px; }
</style>
</head>
<body>
  <section class="card card--front">
    <div class="front-photo" role="img" aria-label="Photo of a high-rise construction site with cranes and a yellow excavator"></div>
    <div class="front-info">
      <h1 class="company-name">
        <span class="company-name__main">VELMAR</span>
        <span class="company-name__sub">CONSTRUCTION LLC</span>
      </h1>
      <p class="person-name">Gerald tomasino</p>
      <p class="address">418 harbor 87th.<br>Dunmoor park ny 10352</p>
      <div class="contact-row">
        <div class="icon-col">
          <svg viewBox="0 0 16 16" aria-hidden="true"><rect width="16" height="16" fill="var(--orange)"/><path d="M5 3.5l2 2-1 1.2a6 6 0 0 0 3.3 3.3l1.2-1 2 2-1.3 1.5C7.5 12.3 3.7 8.5 3.5 4.8z" fill="var(--white)"/></svg>
          <svg viewBox="0 0 16 16" aria-hidden="true"><rect width="16" height="16" fill="var(--orange)"/><rect x="5" y="3" width="6" height="10" rx="1" fill="none" stroke="var(--white)" stroke-width="1.3"/></svg>
          <svg viewBox="0 0 16 16" aria-hidden="true"><rect width="16" height="16" fill="var(--orange)"/><rect x="3" y="4.5" width="10" height="7" fill="none" stroke="var(--white)" stroke-width="1.2"/><path d="M3 4.5l5 4 5-4" fill="none" stroke="var(--white)" stroke-width="1.2"/></svg>
          <svg viewBox="0 0 16 16" aria-hidden="true"><rect width="16" height="16" fill="var(--orange)"/><circle cx="8" cy="8" r="4.6" fill="none" stroke="var(--white)" stroke-width="1.2"/><path d="M3.4 8h9.2M8 3.4c-2 2.6-2 6.6 0 9.2M8 3.4c2 2.6 2 6.6 0 9.2" fill="none" stroke="var(--white)" stroke-width="1"/></svg>
        </div>
        <ul class="contact-list">
          <li>555-318-6094</li>
          <li>555-742-0583</li>
          <li>velmarllc@tridomail.Com</li>
          <li>velmarllc.Com</li>
        </ul>
      </div>
    </div>
  </section>

  <section class="card card--back">
    <div class="brand">
      <div class="brand__square" aria-hidden="true"></div>
      <h2 class="brand__name">
        <span class="brand__main">VELMAR</span>
        <span class="brand__sub">CONSTRUCTION LLC</span>
      </h2>
    </div>
  </section>
</body>
</html>
```